Mousepad Design Creation

We need a round mousepad design. It should have a darker, technology look. Maybe a circuit board or AI feel. It will include our logo, tagline (Let's Up Your Game), and contact information (503.627.CALL (2255) and help@brivanode.com. Attached is one of our current mousepads, as well as our white Q logo. We are just looking for a redesign/update.

```html
<!DOCTYPE html>
<html lang="en">
<head>
<meta charset="utf-8">
<title>Brivanode Mousepad</title>
<link href="https://fonts.googleapis.com/css2?family=Poppins:wght@600;700;800;900&family=Yellowtail&display=swap" rel="stylesheet">
<style>
  :root {
    --page: #ffffff;
    --ink-white: #ffffff;
    --deep: #02030f;
    --navy: #06124a;
    --royal: #1b2fb8;
    --violet: #7a22d6;
    --magenta: #b21ee0;
    --plum: #5a0f7a;
    --lilac: #d07cf0;
    --games-shade: #d9d9de;
    --outline-purple: #6a2ee6;
    --pill-blue: #1c2fa8;
    --pill-purple: #7b1fc4;
  }
  html, body {
    margin: 0;
    width: 693px;
    height: 1200px;
    overflow: hidden;
    background: var(--page);
  }
  .canvas {
    position: relative;
    width: 693px;
    height: 1200px;
  }
  .pad {
    position: absolute;
    left: 46px;
    top: 300px;
    width: 600px;
    height: 600px;
    border-radius: 50%;
    overflow: hidden;
    box-shadow: 0 14px 30px rgba(0,0,0,0.35);
    background:
      radial-gradient(ellipse 70% 45% at 28% 8%, var(--plum) 0%, transparent 70%),
      radial-gradient(ellipse 90% 60% at 75% 10%, var(--violet) 0%, transparent 70%),
      radial-gradient(ellipse 120% 60% at 45% 40%, var(--royal) 0%, transparent 60%),
      linear-gradient(180deg, var(--magenta) 0%, var(--navy) 45%, var(--deep) 72%, #000 100%);
  }
  .skyline {
    position: absolute;
    left: 0; right: 0; bottom: 0;
    height: 250px;
    background:
      linear-gradient(180deg, transparent 0%, rgba(90,30,200,0.25) 60%, rgba(110,40,230,0.55) 100%);
  }
  .brand {
    position: absolute;
    top: 72px;
    left: 0; right: 0;
    display: flex;
    justify-content: center;
    align-items: center;
    gap: 10px;
    color: var(--ink-white);
    font-family: "Poppins", sans-serif;
    font-weight: 700;
    font-size: 30px;
  }
  .brand-dot {
    width: 22px; height: 22px;
    border-radius: 50%;
    background: var(--ink-white);
  }
  .tagline-script {
    position: absolute;
    top: 160px;
    left: 0; right: 0;
    text-align: center;
    font-family: "Yellowtail", cursive;
    font-size: 58px;
    color: var(--ink-white);
    text-shadow: 0 0 12px rgba(190,90,255,0.9);
    padding-left: 20px;
  }
  .tagline-your {
    position: absolute;
    top: 226px;
    left: 0; right: 0;
    text-align: center;
    font-family: "Poppins", sans-serif;
    font-weight: 800;
    font-size: 44px;
    letter-spacing: 1px;
    color: var(--lilac);
    padding-right: 10px;
  }
  .controller {
    position: absolute;
    left: 378px;
    top: 228px;
    width: 120px;
    height: 78px;
    border-radius: 40px 40px 30px 30px;
    background: linear-gradient(160deg, #f2f0f6 0%, #cdb8ee 55%, #8a55c9 100%);
  }
  .tagline-games {
    position: absolute;
    top: 280px;
    left: 0; right: 0;
    text-align: center;
    font-family: "Poppins", sans-serif;
    font-weight: 900;
    font-size: 100px;
    line-height: 1.1;
    letter-spacing: -2px;
    background: linear-gradient(180deg, var(--ink-white) 55%, var(--games-shade) 55%);
    -webkit-background-clip: text;
    background-clip: text;
    color: transparent;
    -webkit-text-stroke: 0;
    filter: drop-shadow(0 0 0 #000) drop-shadow(4px 4px 0 #000) drop-shadow(-4px -4px 0 #000) drop-shadow(3px -3px 0 var(--outline-purple)) drop-shadow(-3px 3px 0 var(--outline-purple));
  }
  .contact {
    position: absolute;
    left: 184px;
    width: 236px;
    height: 28px;
    border-radius: 14px;
    display: flex;
    align-items: center;
    font-family: "Poppins", sans-serif;
    font-weight: 700;
    font-size: 17px;
    color: var(--ink-white);
  }
  .contact-phone {
    top: 420px;
    background: linear-gradient(90deg, var(--pill-blue) 0%, rgba(28,47,168,0.25) 100%);
  }
  .contact-email {
    top: 452px;
    background: linear-gradient(90deg, var(--pill-purple) 0%, rgba(123,31,196,0.25) 100%);
  }
  .contact-icon {
    width: 28px; height: 28px;
    border-radius: 50%;
    background: var(--ink-white);
    display: flex;
    align-items: center;
    justify-content: center;
    margin-right: 9px;
    flex: none;
  }
  .partner-badge {
    position: absolute;
    top: 502px;
    left: 250px;
    width: 100px;
    height: 36px;
    border-radius: 4px;
    background: rgba(255,255,255,0.18);
  }
</style>
</head>
<body>
<div class="canvas">
  <div class="pad">
    <div class="skyline" role="img" aria-label="Neon city skyline of glowing purple and teal light bars"></div>

    <div class="brand"><span class="brand-dot"></span>Brivanode</div>

    <div class="tagline-script">Let's Up</div>
    <div class="tagline-your">YOUR</div>
    <div class="controller" role="img" aria-label="White and purple game controller"></div>
    <div class="tagline-games">GAMES</div>

    <div class="contact contact-phone">
      <span class="contact-icon">
        <svg width="14" height="14" viewBox="0 0 24 24"><path fill="#7b1fc4" d="M6.6 10.8a15 15 0 006.6 6.6l2.2-2.2a1 1 0 011-.25 11.4 11.4 0 003.6.57 1 1 0 011 1V20a1 1 0 01-1 1A17 17 0 013 4a1 1 0 011-1h3.5a1 1 0 011 1c0 1.25.2 2.45.57 3.57a1 1 0 01-.25 1z"/></svg>
      </span>503.627.CALL (2255)
    </div>
    <div class="contact contact-email">
      <span class="contact-icon">
        <svg width="14" height="12" viewBox="0 0 24 18"><rect x="1" y="1" width="22" height="16" rx="2" fill="#7b1fc4"/><path d="M2 2l10 8 10-8" stroke="#fff" stroke-width="2" fill="none"/></svg>
      </span>help@brivanode.com
    </div>

    <div class="partner-badge"></div>
  </div>
</div>
</body>
</html>
```